Billboard design - consider what a billboard is

Design a billboard using my logo - Billboard is 6m x 3m
A Billboard is advertising for my company that is on a big sign.

Has to be clean and easy to read, and ideally highlights that we are Residential and Commercial builders.

Keep it clean and easy to read

The contact number for the board is

027 584 9071
www.fernridgebuildworks.co.nz
info@fernridgebuildworks.co.nz

Doesnt have to have all contact details if it doesnt fit

Has to catch peoples attention to contact us if they need a builder

Can you please change the sign to be all white writing, with black background ?
Updates

Please consider what a billboard is...

The design needs to be suitable for a billboard..

Target Market(s)

people driving past

Industry/Entity Type

Construction

Logo Text

Wellington Builder, website email address, contact number

Colors
0054AA
0677BA
7BADD7
CADEEF
E8F1F8

Requirements
Must have
• Easy to read
Nice to have
• easy to read, can clearly see contact details

```html
<!DOCTYPE html>
<html lang="en">
<head>
<meta charset="UTF-8">
<title>Fernridge Buildworks Billboard</title>
<link rel="stylesheet" href="https://fonts.googleapis.com/css2?family=Poppins:wght@500;600;700;800&display=swap">
<style>
  :root {
    --page-bg: #e8f1f8;
    --board-navy: #1e2048;
    --headline-white: #ffffff;
    --subtitle-white: #eef0f6;
    --callout-yellow: #f6cf2a;
    --logo-blue: #0054aa;
    --sky-top: #7badd7;
    --sky-mid: #cadeef;
    --site-grey: #9a9ea6;
    --site-dark: #5c5f66;
  }
  * { margin: 0; padding: 0; box-sizing: border-box; }
  html, body {
    width: 1200px;
    height: 800px;
    overflow: hidden;
    background: var(--page-bg);
    font-family: "Poppins", sans-serif;
  }
  .billboard {
    position: absolute;
    left: 20px;
    top: 111px;
    width: 1160px;
    height: 578px;
    background: var(--board-navy);
    overflow: hidden;
  }
  .billboard__photo {
    position: absolute;
    inset: 0;
    width: 1160px;
    height: 578px;
  }
  .billboard__copy {
    position: absolute;
    left: 29px;
    white-space: nowrap;
    line-height: 1;
  }
  .headline {
    color: var(--headline-white);
    font-weight: 800;
    font-size: 58px;
    letter-spacing: 1px;
  }
  .headline--1 { top: 24px; }
  .headline--2 { top: 97px; }
  .headline--3 { top: 171px; }
  .subtitle {
    top: 256px;
    color: var(--subtitle-white);
    font-weight: 600;
    font-size: 38px;
    letter-spacing: 1px;
  }
  .callout {
    color: var(--callout-yellow);
    font-weight: 600;
    font-size: 41px;
    letter-spacing: 1.5px;
  }
  .callout--1 { top: 348px; }
  .callout--2 { top: 397px; }
  .phone {
    top: 457px;
    color: var(--headline-white);
    font-weight: 700;
    font-size: 42px;
  }
  .website {
    top: 525px;
    color: var(--subtitle-white);
    font-weight: 500;
    font-size: 25px;
    letter-spacing: 0.8px;
  }
  .logo-panel {
    position: absolute;
    left: 953px;
    top: 417px;
    width: 178px;
    height: 132px;
    background: #ffffff;
    display: flex;
    align-items: center;
    justify-content: center;
  }
  .logo-panel__name {
    color: var(--logo-blue);
    font-weight: 700;
    font-size: 24px;
  }
</style>
</head>
<body>
  <section class="billboard">
    <svg class="billboard__photo" viewBox="0 0 1160 578" role="img" aria-label="Photo of a multi-storey commercial building under scaffolding and wrap on a Wellington city site, with blue sky and neighbouring apartment towers">
      <defs>
        <linearGradient id="siteTones" x1="0" y1="0" x2="0" y2="1">
          <stop offset="0" stop-color="var(--sky-top)"/>
          <stop offset="0.35" stop-color="var(--sky-mid)"/>
          <stop offset="0.7" stop-color="var(--site-grey)"/>
          <stop offset="1" stop-color="var(--site-dark)"/>
        </linearGradient>
      </defs>
      <path d="M742 0 C560 120 540 460 742 578 L1160 578 L1160 0 Z" fill="url(#siteTones)"/>
    </svg>

    <div class="billboard__copy headline headline--1">RESIDENTIAL &amp;</div>
    <div class="billboard__copy headline headline--2">COMMERCIAL</div>
    <div class="billboard__copy headline headline--3">BUILDERS</div>
    <div class="billboard__copy subtitle">Wellington Builder</div>
    <div class="billboard__copy callout callout--1">NEED A BUILDER?</div>
    <div class="billboard__copy callout callout--2">CALL US TODAY!</div>
    <div class="billboard__copy phone">027 584 9071</div>
    <div class="billboard__copy website">www.fernridgebuildworks.co.nz</div>

    <div class="logo-panel">
      <span class="logo-panel__name">Fernridge</span>
    </div>
  </section>
</body>
</html>
```